Business Flyer

I want an updated flyer that will have the same content as the one attached but in a different format. They flyers will be passed out to the community and local businesses.

```html
<!DOCTYPE html>
<html lang="en">
<head>
<meta charset="UTF-8">
<title>Maple Grove Juicery – Community Flyer</title>
<link rel="stylesheet" href="https://fonts.googleapis.com/css2?family=Rubik:wght@900&family=Open+Sans:wght@600;700&family=Roboto+Condensed:wght@400&display=swap">
<style>
  :root {
    --stage: #d9d9d9;
    --paper-top: #f9d7a6;
    --paper-mid: #fdf0de;
    --paper-low: #fffaf3;
    --green: #1f9a4a;
    --brown: #a0621a;
    --orange: #f49a1c;
    --purple: #7a2a8f;
    --plum: #4a1247;
    --band: #f7ac3a;
    --juice-light: #fde48a;
    --juice-deep: #f6a21e;
    --body-text: #4a3b33;
    --white: #ffffff;
  }
  * { box-sizing: border-box; margin: 0; padding: 0; }
  html, body {
    width: 1200px; height: 1200px; overflow: hidden;
    background: var(--stage);
  }
  .canvas {
    width: 1200px; height: 1200px;
    display: flex; align-items: center; justify-content: center;
  }
  .flyer {
    position: relative;
    width: 820px; height: 1100px;
    overflow: hidden;
    background: linear-gradient(180deg, var(--paper-top) 0%, var(--paper-mid) 38%, var(--paper-low) 65%);
  }
  .headline {
    position: absolute; top: 80px; left: 0; right: 0;
    text-align: center;
    font-family: "Rubik", sans-serif; font-weight: 900;
    text-transform: uppercase; line-height: 1.08; letter-spacing: 0.5px;
  }
  .headline .line { display: block; font-size: 56px; white-space: nowrap; }
  .headline .natural { color: var(--green); font-size: 64px; }
  .headline .cold-press { color: var(--brown); }
  .headline .juices { color: var(--orange); }
  .headline .delicious { color: var(--purple); }
  .headline .smoothies { color: var(--plum); }
  .intro {
    position: absolute; top: 300px; left: 80px; right: 80px;
    text-align: center;
    font-family: "Open Sans", sans-serif; font-weight: 600;
    font-size: 17px; line-height: 1.55; color: var(--body-text);
  }
  .brand-mark {
    position: absolute; top: 470px; right: 80px;
    display: flex; align-items: center; gap: 12px;
  }
  .brand-mark .dot {
    width: 22px; height: 22px; border-radius: 50%; background: var(--orange);
  }
  .brand-mark .name {
    font-family: "Open Sans", sans-serif; font-weight: 700;
    font-size: 30px; color: var(--brown);
  }
  .juice-visual {
    position: absolute; left: 0; top: 560px; width: 600px; height: 540px;
    background:
      radial-gradient(circle at 58% 30%, var(--juice-light) 0%, rgba(253,228,138,0.6) 20%, rgba(253,228,138,0) 45%),
      radial-gradient(ellipse at 42% 88%, var(--juice-deep) 0%, rgba(246,162,30,0.8) 32%, rgba(246,162,30,0) 65%);
    z-index: 2;
  }
  .band {
    position: absolute; left: 0; right: 0; bottom: 0; height: 200px;
    background: var(--band); z-index: 1;
  }
  .address {
    position: absolute; right: 50px; bottom: 80px; z-index: 3;
    font-family: "Roboto Condensed", sans-serif; font-weight: 400;
    font-size: 38px; color: var(--white); white-space: nowrap;
  }
  .socials {
    position: absolute; right: 50px; top: 795px; z-index: 3;
    font-family: "Roboto Condensed", sans-serif; font-weight: 400;
    font-size: 26px; color: var(--purple);
    display: flex; flex-direction: column; align-items: flex-end; gap: 10px;
  }
  .socials .item { display: flex; align-items: center; gap: 12px; }
  .socials .badge {
    width: 28px; height: 28px; border-radius: 6px; background: var(--purple);
  }
</style>
</head>
<body>
<div class="canvas">
  <article class="flyer">
    <h1 class="headline">
      <span class="line natural">Natural</span>
      <span class="line"><span class="cold-press">Cold Press</span> <span class="juices">Juices and</span></span>
      <span class="line"><span class="delicious">Delicious</span> <span class="smoothies">Smoothies</span></span>
    </h1>

    <p class="intro">Thank you for supporting your local business as we aim to provide you with a comfortable and inviting place coupled with great products that is conductive to changing people’s lives and creating a possitive community through our offering of natural cold press juice and delicious smoothies.</p>

    <div class="brand-mark">
      <span class="dot"></span>
      <span class="name">Maple Grove Juicery</span>
    </div>

    <div class="juice-visual" role="img" aria-label="Glass of fresh orange juice with a straw and an orange slice, surrounded by a bright juice splash"></div>

    <div class="socials">
      <div class="item"><span>Maple Grove Juicery</span><span class="badge"></span></div>
      <div class="item"><span>MAPLEGROVE.JUICERY</span><span class="badge"></span></div>
    </div>

    <div class="band"></div>
    <p class="address">1480 Orchard Lane, Millbrook, MD 20999</p>
  </article>
</div>
</body>
</html>
```